Modern card design needed for building development company

We are looking for a sharp modern new look for our business cards.
We are a New Zealand based company called TKR Ventures NZ LTD that specialises in subdividing large sections, housing and commercial buildings.
We have attached a photo of the current logo and would like to see it improved somehow as it looks a bit dated.
We are open to any colours.

Target Market(s)

Investors, Property buyers

Industry/Entity Type

Investment

Contact Information for Business Card

TKR VENTURES NZ LTD
www.tkrventuresnz.example.nz

Dorian Fletcher
Phone +64 21 843 209
Email dpfletcher@mailvane.example.nz

Font styles to use
Serif
Sans Serif

Colors
0792cd
33a6d7
85cae6
6b449b
886aae
f04a50
ec1f27
f37122
f68d4d

Requirements
Must have
• Please try and make the logo more modern or if you have a similar one we would like to see it.

```html
<!DOCTYPE html>
<html lang="en">
<head>
<meta charset="utf-8">
<title>TKR Ventures NZ LTD — Business Card</title>
<link rel="stylesheet" href="https://fonts.googleapis.com/css2?family=Jost:wght@400;500&display=swap">
<style>
  :root {
    --backdrop: #d4d6d5;
    --brand-red: #941a2c;
    --paper: #ffffff;
    --ink: #262626;
    --ink-soft: #3a3a3a;
    --rule: #4a4a4a;
    --card-shadow: 0 10px 28px rgba(0, 0, 0, 0.22);
  }
  * { box-sizing: border-box; margin: 0; padding: 0; }
  html, body {
    width: 1200px; height: 904px; overflow: hidden;
    background: var(--backdrop);
    font-family: "Jost", "Futura", sans-serif;
  }
  .stage { position: relative; width: 1200px; height: 904px; }
  .card {
    position: absolute;
    width: 620px; height: 354px;
    box-shadow: var(--card-shadow);
  }

  /* Front */
  .card-front {
    left: 90px; top: 70px;
    background: var(--brand-red);
    color: var(--paper);
    display: flex; flex-direction: column; align-items: center; justify-content: center;
  }
  .front-brand {
    display: flex; align-items: center; gap: 14px;
    font-size: 26px; font-weight: 400; letter-spacing: 2px;
    margin-top: 20px;
  }
  .brand-square { width: 22px; height: 22px; background: currentColor; }
  .front-web {
    margin-top: 62px;
    font-size: 14px; letter-spacing: 1.5px;
  }

  /* Back */
  .card-back {
    left: 490px; top: 480px;
    background: var(--paper);
    color: var(--ink);
  }
  .back-brand {
    position: absolute; right: 40px; top: 58px;
    display: flex; align-items: center; gap: 10px;
    font-size: 17px; letter-spacing: 1.5px;
    color: var(--ink-soft);
  }
  .back-brand .brand-square { width: 16px; height: 16px; background: var(--brand-red); }
  .divider {
    position: absolute; left: 118px; right: 36px; top: 186px;
    height: 1px; background: var(--rule);
  }
  .accent-bar {
    position: absolute; left: 0; top: 152px;
    width: 20px; height: 56px; background: var(--brand-red);
  }
  .holder { position: absolute; left: 118px; top: 138px; }
  .holder-name { font-size: 30px; font-weight: 500; line-height: 1.1; color: var(--ink); }
  .holder-role {
    position: absolute; top: 54px; left: 0; white-space: nowrap;
    font-size: 20px; color: var(--brand-red);
  }
  .contacts {
    position: absolute; left: 56px; top: 248px;
    list-style: none; font-size: 16px; line-height: 26px;
  }
  .contacts li { display: flex; align-items: center; gap: 14px; }
  .contacts svg { width: 16px; height: 16px; flex: none; }
  .contacts .web-highlight { color: var(--brand-red); }
  .address {
    position: absolute; right: 40px; top: 198px;
    text-align: right; font-size: 15px; line-height: 20px;
  }
  .address-label { font-weight: 500; }
</style>
</head>
<body>
<main class="stage">
  <section class="card card-front">
    <div class="front-brand"><span class="brand-square"></span>TKR VENTURES NZ LTD</div>
    <p class="front-web">www.tkrventuresnz.example.nz</p>
  </section>

  <section class="card card-back">
    <div class="back-brand"><span class="brand-square"></span>TKR VENTURES NZ LTD</div>
    <div class="accent-bar"></div>
    <div class="holder">
      <h1 class="holder-name">Dorian Fletcher</h1>
      <p class="holder-role">Founder/CEO</p>
    </div>
    <div class="divider"></div>
    <address class="address">
      <span class="address-label">Address:</span><br>
      Your Street Address,<br>
      New Zealand, 1234
    </address>
    <ul class="contacts">
      <li>
        <svg viewBox="0 0 16 16" aria-hidden="true"><path d="M4 1.5l2.5 3-1.5 1.5c.8 2 2.5 3.7 4.5 4.5l1.5-1.5 3 2.5-1.5 2.5C7 14 2 9 1.5 3z" fill="#941a2c"/></svg>
        +64 21 843 209
      </li>
      <li>
        <svg viewBox="0 0 16 16" aria-hidden="true"><rect x="1.5" y="3.5" width="13" height="9" fill="none" stroke="#941a2c" stroke-width="1.5"/><path d="M1.5 3.5L8 9l6.5-5.5" fill="none" stroke="#941a2c" stroke-width="1.5"/></svg>
        dpfletcher@mailvane.example.nz
      </li>
      <li>
        <svg viewBox="0 0 16 16" aria-hidden="true"><circle cx="8" cy="8" r="6.5" fill="none" stroke="#941a2c" stroke-width="1.3"/><ellipse cx="8" cy="8" rx="3" ry="6.5" fill="none" stroke="#941a2c" stroke-width="1.1"/><path d="M1.5 8h13" stroke="#941a2c" stroke-width="1.1"/></svg>
        <span>www.<span class="web-highlight">tkrventuresnz</span>.example.nz</span>
      </li>
    </ul>
  </section>
</main>
</body>
</html>
```